New Update: I am changing the title of the book and the back cover text. Title was too long before. Same style as before.
New Title: Under the Quiet Sky
New Subtitle: A Gardener’s Notes on Patience (italics on front cover)

Back cover text:
Under the Quiet Sky: A Gardener’s Notes on Patience offers clear, compassionate guidance for those recovering from total loss. Drawing from his experience as a Brennick Flood survivor, Tobias Quellhorst shares practical advice on insurance, rebuilding, and emotional healing, along with lessons in strength and community. This is not a book about tragedy; it’s about perseverance and renewal. Under the Quiet Sky is a trusted companion for anyone rebuilding life, home, and hope after disaster.

Font styles to use
Serif

Colors
EB3D1F
EC4F4E
F09395
F8D3D4
FCEDEE

Requirements
Should not have
• No pictures or anything related to fire on the cover.

```html
<!DOCTYPE html>
<html lang="en">
<head>
<meta charset="utf-8">
<title>Under the Quiet Sky — Book Cover</title>
<link rel="stylesheet" href="https://fonts.googleapis.com/css2?family=Cinzel:wght@400;500&family=Cormorant+Garamond:ital,wght@1,500&family=Crimson+Text:wght@400&display=swap">
<style>
  :root {
    --wine-dark: #45000a;
    --wine: #7a0008;
    --wine-bright: #990000;
    --spine: #5a0a10;
    --blush: #fbeeef;
    --gold-light: #f2cf96;
    --gold: #e4b05c;
    --title-red: #9b0010;
    --ink: #1c1c1c;
    --white: #ffffff;
  }
  * { margin: 0; padding: 0; box-sizing: border-box; }
  html, body { width: 1200px; height: 859px; overflow: hidden; background: var(--white); }
  .cover { position: relative; width: 1200px; height: 859px; overflow: hidden; }

  /* Back cover */
  .back {
    position: absolute; left: 0; top: 0; width: 572px; height: 859px;
    background: linear-gradient(180deg, var(--wine-dark) 0%, var(--wine) 45%, var(--wine-bright) 100%);
    color: var(--white);
  }
  .back-title {
    position: absolute; left: 0; top: 40px; width: 572px; text-align: center;
    font-family: "Cinzel", serif; font-size: 31px; line-height: 39px; font-weight: 400;
  }
  .back-copy {
    position: absolute; left: 70px; top: 170px; width: 436px;
    font-family: "Crimson Text", serif; font-size: 15.6px; line-height: 19px;
    text-align: justify; hyphens: auto;
  }
  .back-copy p + p { margin-top: 19px; }
  .back-rule { position: absolute; left: 70px; top: 401px; width: 432px; height: 2px; background: var(--white); }
  .author-photo {
    position: absolute; left: 69px; top: 429px; width: 85px; height: 107px;
    border: 2px solid var(--white);
    background: linear-gradient(180deg, #d9d4c4 0%, #b9a99a 55%, #1d2330 100%);
  }
  .author-bio {
    position: absolute; left: 163px; top: 426px; width: 343px;
    font-family: "Crimson Text", serif; font-size: 14.4px; line-height: 17.5px;
    text-align: justify;
  }

  /* Spine */
  .spine {
    position: absolute; left: 572px; top: 0; width: 56px; height: 859px;
    background: linear-gradient(180deg, #4f0a10 0%, var(--spine) 40%, #8e0006 100%);
  }
  .spine svg { position: absolute; left: 0; top: 0; }

  /* Front cover */
  .front {
    position: absolute; left: 628px; top: 0; width: 572px; height: 859px;
    background: linear-gradient(180deg, #5a0a0e 55%, var(--wine) 70%, var(--wine-bright) 100%);
  }
  .front svg.front-art { position: absolute; left: 0; top: 0; }
  .emblem {
    position: absolute; left: 106px; top: 45px; width: 363px; height: 110px;
    background: linear-gradient(180deg, rgba(242,207,150,0.45), rgba(228,176,92,0.3));
    border-radius: 4px;
  }
  .tagline {
    position: absolute; left: 0; top: 632px; width: 572px; padding-left: 58px;
    font-family: "Cinzel", serif; font-size: 30px; line-height: 38px; color: var(--white);
  }
  .front-rule { position: absolute; left: 58px; top: 722px; width: 436px; height: 2px; background: var(--white); }
  .front-author {
    position: absolute; left: 0; top: 770px; width: 572px; text-align: center;
    font-family: "Cinzel", serif; font-size: 40px; line-height: 50px; color: var(--white);
  }
</style>
</head>
<body>
<main class="cover">

  <section class="back">
    <h2 class="back-title">Under the Quiet Sky<br>A Gardener’s Notes on Patience</h2>
    <div class="back-copy">
      <p>Under the Quiet Sky: A Gardener’s Notes on Patience offers clear, compassionate guidance for those recovering from total loss. Drawing from his experience as a Brennick Flood survivor, Tobias Quellhorst shares practical advice on insurance, rebuilding, and emotional healing, along with lessons in strength and community.</p>
      <p>This is not a book about tragedy; it’s about perseverance and renewal.</p>
      <p>Under the Quiet Sky is a trusted companion for anyone rebuilding life, home, and hope after disaster.</p>
    </div>
    <div class="back-rule"></div>
    <div class="author-photo" role="img" aria-label="Portrait photograph of the author"></div>
    <p class="author-bio">Tobias Quellhorst is a Realtor with Summit Ridge Realty in Colorado. Combining his own sales training, his interviews with many top Agents and Trainers in the real estate industry and over 30 years sales experience Tobias Quellhorst has insights into the trends within the real estate industry. Tobias has synthesized his findings on how to effectively build, grow and maintain a profitable business for Real Estate Agents in a way where they believe in themselves, enjoy their work, love their career and enjoy living a balanced life. He lives in the Boulder, Colorado area.</p>
  </section>

  <section class="spine">
    <svg width="56" height="859" viewBox="0 0 56 859">
      <text transform="translate(18 62) rotate(90)" textLength="540" lengthAdjust="spacingAndGlyphs"
            font-family="Cinzel, serif" font-size="27" fill="#ffffff">Under the Quiet Sky: A Gardener’s Notes on Patience</text>
      <text transform="translate(21 645) rotate(90)" textLength="170" lengthAdjust="spacingAndGlyphs"
            font-family="Cinzel, serif" font-size="20" fill="#ffffff">Tobias Quellhorst</text>
    </svg>
  </section>

  <section class="front">
    <svg class="front-art" width="572" height="859" viewBox="0 0 572 859">
      <defs>
        <linearGradient id="goldFill" x1="0" y1="0" x2="1" y2="0">
          <stop offset="0" stop-color="#e0a94f"/>
          <stop offset="0.5" stop-color="#f2cf96"/>
          <stop offset="1" stop-color="#e2ad58"/>
        </linearGradient>
      </defs>
      <path d="M0 0 H572 V548 C540 552 520 560 490 566 C455 574 430 560 400 572 C370 584 340 570 310 578 C280 586 250 572 220 566 C190 560 160 576 130 566 C100 556 80 540 55 546 C35 550 20 545 0 550 Z" fill="#fbeeef"/>
      <path d="M0 522 C15 530 25 540 45 536 C75 530 95 548 130 556 C160 564 190 548 220 556 C250 564 280 578 310 570 C340 562 370 576 400 564 C430 552 455 566 490 558 C520 552 540 542 572 538 V548 C540 552 520 560 490 566 C455 574 430 560 400 572 C370 584 340 570 310 578 C280 586 250 572 220 566 C190 560 160 576 130 566 C100 556 80 540 55 546 C35 550 20 545 0 550 Z" fill="#ffffff"/>
      <text x="53" y="230" textLength="454" lengthAdjust="spacingAndGlyphs" font-family="Cinzel, serif" font-size="84" fill="url(#goldFill)">UNDER THE</text>
      <text x="53" y="326" textLength="454" lengthAdjust="spacingAndGlyphs" font-family="Cinzel, serif" font-size="112" fill="#9b0010">QUIET</text>
      <text x="53" y="437" textLength="454" lengthAdjust="spacingAndGlyphs" font-family="Cinzel, serif" font-size="122" fill="url(#goldFill)">SKY</text>
      <line x1="59" y1="479" x2="82" y2="479" stroke="#1c1c1c" stroke-width="1.6"/>
      <line x1="490" y1="479" x2="513" y2="479" stroke="#1c1c1c" stroke-width="1.6"/>
      <text x="286" y="490" text-anchor="middle" font-family="'Cormorant Garamond', serif" font-style="italic" font-weight="500" font-size="35" fill="#1c1c1c">A Gardener’s Notes on Patience</text>
    </svg>
    <div class="emblem" role="img" aria-label="Gold line emblem of a house"></div>
    <p class="tagline">A Journey Through Loss,<br>Recovery, and Rebuilding</p>
    <div class="front-rule"></div>
    <p class="front-author">Tobias Quellhorst</p>
  </section>

</main>
</body>
</html>
```